Redesign responsive website and logo for webshop platform

Redesign our applications old website with a new clean, crisp modern looking style that is responsive.

Our application is a cloud based, free ecommerce platform that lets users set up their own webshops within minutes. (Similar to Mabrook https://mabrook.example/l/sell)

Our old website: http://sv.vendlyx.example/

I need redesigned HTML + CSS for the following three pages:
* Landing Page:
(Old page: http://sv.vendlyx.example/)
I have attached a mockup of a proposed layout/structure for the landing page.
- Pricing comparision/features page
(Old page http://sv.vendlyx.example/t/funktioner)
- Generic "article" page:
(Old page http://sv.vendlyx.example/d/redigerasida)

The pages must responsive using HTML 5/CSS 3 (I prefer Bootstrap 3 if possible).

I also need a redesign of the logotype.

If you have any questions don't hesitate to ask and we will provide whatever is needed to you.

Logo Text

Vendlyx

Coding

Coded - Design and coding required

Number of Pages Required

3 page

Font styles to use
Serif
Sans Serif

```html
<!DOCTYPE html>
<html lang="en">
<head>
<meta charset="utf-8">
<title>Vendlyx – Start A Free Webshop</title>
<link rel="stylesheet" href="https://fonts.googleapis.com/css2?family=Roboto:wght@300;400;500;700&family=Open+Sans:wght@400;600;700&family=Noto+Serif:wght@400;700&display=swap">
<style>
:root{
  --blue:#0a6fcc;
  --blue-dark:#075fb0;
  --yellow:#f7d923;
  --gold-line:#e4c52a;
  --cream:#fdf8dd;
  --ink:#2b2b2b;
  --muted:#6f6f6f;
  --panel:#2a2d30;
  --panel-line:#41454a;
  --footer:#242628;
  --white:#ffffff;
}
*{box-sizing:border-box;margin:0;padding:0}
html,body{width:1200px;height:2936px;overflow:hidden}
body{position:relative;background:var(--white);font-family:"Roboto",Arial,sans-serif;color:var(--ink)}

/* header */
.site-header{position:absolute;left:0;top:0;width:1200px;height:78px;background:rgba(255,255,255,.9);z-index:2}
.brand{position:absolute;left:190px;top:20px;display:flex;align-items:center;gap:8px;font-family:"Open Sans",sans-serif;font-weight:700;font-size:27px;color:var(--blue)}
.brand-mark{width:16px;height:16px;background:var(--blue);border-radius:3px}
.nav-mail,.nav-login{position:absolute;top:30px;font-family:"Open Sans",sans-serif;font-size:13px;color:#333;display:flex;align-items:center;gap:7px;white-space:nowrap}
.nav-mail{left:654px}
.nav-login{left:846px}
.btn-start{position:absolute;left:926px;top:22px;width:100px;height:36px;background:var(--blue);color:#fff;border-radius:3px;font-family:"Noto Serif",serif;font-size:11px;display:flex;align-items:center;justify-content:center;letter-spacing:.3px}

/* hero */
.hero-photo{position:absolute;left:0;top:0;width:1200px;height:493px;background:linear-gradient(100deg,#7a4a36 0%,#b89a82 25%,#e9e1d6 48%,#d6cabb 70%,#8f7a66 100%)}
.hero-card{position:absolute;left:182px;top:202px;width:423px;height:199px;background:rgba(25,25,25,.85);padding:22px 16px;color:#fff}
.hero-card h1{font-family:"Open Sans",sans-serif;font-weight:700;font-size:19px}
.hero-card .rule{width:164px;height:3px;background:var(--blue);margin:6px 0 12px}
.hero-card p{font-family:"Open Sans",sans-serif;font-size:11.5px;line-height:20px;color:#ddd}
.btn-yellow{display:inline-flex;align-items:center;justify-content:center;background:var(--yellow);color:#222;font-family:"Noto Serif",serif;border-radius:20px}
.hero-card .btn-yellow{margin-top:10px;width:148px;height:30px;font-size:11px}

/* why */
.section-title{position:absolute;left:0;width:1200px;text-align:center;font-weight:300;font-size:28px;color:#333}
.why-title{top:550px}
.feature{position:absolute}
.feature h3{font-weight:300;font-size:25px;color:#222;margin-bottom:10px;white-space:nowrap}
.feature p{font-size:13px;line-height:21px;color:var(--muted)}
.feature.left{left:245px;width:330px}
.feature.right{left:680px;width:347px;text-align:right}
.icon-ring{position:absolute;width:52px;height:52px;border:2px solid var(--blue);border-radius:50%;display:flex;align-items:center;justify-content:center}
.icon-ring.left{left:170px}
.icon-ring.right{left:608px}

/* features */
.features-band{position:absolute;left:0;top:1108px;width:1200px;height:730px;background:var(--cream)}
.band-lead{position:absolute;left:0;width:1200px;text-align:center;font-size:13.5px;line-height:21px;color:#444}
.features-panel{position:absolute;left:172px;top:1296px;width:354px;height:432px;background:var(--panel);color:#fff;padding:32px 26px}
.features-panel h2{font-weight:400;font-size:27px}
.features-panel .rule{width:44px;height:3px;background:var(--yellow);margin:12px 0 24px}
.features-panel p{font-size:12.5px;line-height:19px;color:#ddd;margin-bottom:14px}
.feature-list{list-style:none}
.feature-list li{display:flex;justify-content:space-between;align-items:center;height:37.5px;border-bottom:1px solid var(--panel-line);font-size:12px;font-weight:700}
.feature-list li:last-child{border-bottom:none}
.photo-celebrate{position:absolute;left:526px;top:1296px;width:501px;height:432px;background:linear-gradient(180deg,#f3eee7 0%,#ece3d6 70%,#b8956e 100%)}
.btn-outline{position:absolute;display:flex;align-items:center;justify-content:center;border:2px solid var(--gold-line);border-radius:25px;font-family:"Noto Serif",serif;font-size:13px;color:#333;background:transparent;letter-spacing:.4px}

/* growing */
.photo-store{position:absolute;left:172px;top:2010px;width:855px;height:286px;background:linear-gradient(90deg,#6b5a3a 0%,#a89670 30%,#7d8a5a 55%,#5a4a3c 80%,#3d3530 100%)}

/* devices */
.device-band{position:absolute;left:0;top:2407px;width:1200px;height:474px;background:var(--blue)}
.device-band h2{position:absolute;left:198px;top:60px;font-weight:300;font-size:31px;line-height:38px;color:#fff}
.device-band .rule{position:absolute;left:198px;top:145px;width:46px;height:3px;background:var(--yellow)}
.device-band p{position:absolute;left:198px;top:172px;width:400px;font-size:13.5px;line-height:20px;color:#e6efff}
.device-band .btn-yellow{position:absolute;left:200px;top:274px;width:229px;height:47px;font-size:14px;border-radius:25px}
.device-preview{position:absolute;left:744px;top:43px;width:188px;height:384px;border-radius:30px;background:linear-gradient(180deg,#f4f4f4,#dcdcdc)}

/* footer */
.site-footer{position:absolute;left:0;top:2881px;width:1200px;height:55px;background:var(--footer);color:#ddd;font-size:12px}
.site-footer .copy{position:absolute;left:186px;top:20px}
.social{position:absolute;left:955px;top:21px;display:flex;gap:16px}
.social span{width:13px;height:13px;border-radius:50%;background:#e5e5e5}
</style>
</head>
<body>

<div class="hero-photo" role="img" aria-label="Photo of a bright retail clothing and shoe store interior with shelves of caps and a brick wall"></div>

<header class="site-header">
  <div class="brand"><span class="brand-mark"></span>Vendlyx</div>
  <div class="nav-mail">
    <svg width="16" height="14" viewBox="0 0 16 14"><path d="M1 6 15 1 11 13 8 8Z" fill="none" stroke="#0a6fcc" stroke-width="1.4" stroke-linejoin="round"/></svg>
    info@vendlyx.example
  </div>
  <div class="nav-login">
    <svg width="12" height="14" viewBox="0 0 12 14"><rect x="1" y="1" width="10" height="12" fill="none" stroke="#0a6fcc" stroke-width="1.4"/><path d="M4 7h5" stroke="#0a6fcc" stroke-width="1.4"/></svg>
    Log in
  </div>
  <a class="btn-start">GET STARTED</a>
</header>

<section class="hero-card">
  <h1>Start A Free Webshop</h1>
  <div class="rule"></div>
  <p>Vendlyx is a service that allows you to launch a complete online store. The service is free and has everything needed to get you started with your business and sell products online.</p>
  <a class="btn-yellow">CREATE WEBSHOP &raquo;</a>
</section>

<h2 class="section-title why-title">Why Choose Us</h2>

<div class="icon-ring left" style="top:648px"><svg width="26" height="26" viewBox="0 0 26 26"><circle cx="13" cy="13" r="10" fill="none" stroke="#0a6fcc" stroke-width="2"/><path d="M13 7v6h5" fill="none" stroke="#0a6fcc" stroke-width="2"/></svg></div>
<div class="feature left" style="top:650px"><h3>Get started in 5 minutes</h3><p>Starting an E-cart with Vendlyx takes no more than 5 minutes. Create an account to get started. Nothing needs to be installed on your computer.</p></div>

<div class="icon-ring right" style="top:648px"><svg width="26" height="26" viewBox="0 0 26 26"><path d="M3 5h4l3 11h11l2-8H8" fill="none" stroke="#0a6fcc" stroke-width="2" stroke-linejoin="round"/><circle cx="11" cy="21" r="2" fill="#0a6fcc"/><circle cx="19" cy="21" r="2" fill="#0a6fcc"/></svg></div>
<div class="feature right" style="top:650px"><h3>Create a free online store</h3><p>Vendlyx is a free service. The service has no monthly<br>fees or transaction charges on what you sell.</p></div>

<div class="icon-ring left" style="top:817px"><svg width="26" height="26" viewBox="0 0 26 26"><rect x="4" y="5" width="18" height="16" fill="none" stroke="#0a6fcc" stroke-width="2"/><path d="M4 10h18M9 14h4v4H9z" fill="none" stroke="#0a6fcc" stroke-width="2"/></svg></div>
<div class="feature left" style="top:809px"><h3>Intuitive user interface</h3><p>It is fast to add new products. Organize products by<br>drag and drop.</p></div>

<div class="icon-ring right" style="top:817px"><svg width="26" height="26" viewBox="0 0 26 26"><path d="M4 20 10 12l5 5 7-10" fill="none" stroke="#0a6fcc" stroke-width="2" stroke-linejoin="round"/><circle cx="10" cy="12" r="2" fill="#0a6fcc"/><circle cx="15" cy="17" r="2" fill="#0a6fcc"/></svg></div>
<div class="feature right" style="top:809px"><h3>Search engine optimized</h3><p>Vendlyx is consistently created with search engine<br>optimization as a focus point.</p></div>

<div class="icon-ring left" style="top:960px"><svg width="26" height="26" viewBox="0 0 26 26"><path d="M6 20l2-6L18 4l4 4-10 10z M8 14l4 4" fill="none" stroke="#0a6fcc" stroke-width="2" stroke-linejoin="round"/></svg></div>
<div class="feature left" style="top:952px"><h3>Design your shop</h3><p>Choose from finished appearance templates or create<br>your own graphic profile with a few clicks.</p></div>

<div class="icon-ring right" style="top:960px"><svg width="26" height="26" viewBox="0 0 26 26"><rect x="4" y="5" width="18" height="13" fill="none" stroke="#0a6fcc" stroke-width="2"/><path d="M8 9h10M8 13h7M13 18v4M9 22h8" fill="none" stroke="#0a6fcc" stroke-width="2"/></svg></div>
<div class="feature right" style="top:952px"><h3>Smart Dashboard</h3><p>On the home page of your online store, you get an<br>overview about the last incoming orders, analysis<br>and statistics</p></div>

<section class="features-band"></section>
<h2 class="section-title" style="top:1160px">All The Features You Need for Your Webshop</h2>
<p class="band-lead" style="top:1211px">Nam libero tempore cum soluta nobis est eligendi optio cumque nihil impedit quo minus<br>id quod maxime placeat facere possimus omnis voluptas assumenda est</p>

<div class="features-panel">
  <h2>Features</h2>
  <div class="rule"></div>
  <p>Temporibus autem quibusdam et aut officiis debitis rerum necessitatibus saepe eveniet ut et voluptates repudiandae sint et molestiae non recusandae.</p>
  <ul class="feature-list">
    <li>Unlimited number of products<svg width="14" height="11" viewBox="0 0 14 11"><path d="M1 6l4 4 8-9" fill="none" stroke="#8fc35a" stroke-width="1.6"/></svg></li>
    <li>Unlimited data traffic<svg width="14" height="11" viewBox="0 0 14 11"><path d="M1 6l4 4 8-9" fill="none" stroke="#8fc35a" stroke-width="1.6"/></svg></li>
    <li>Basic Design News<svg width="14" height="11" viewBox="0 0 14 11"><path d="M1 6l4 4 8-9" fill="none" stroke="#8fc35a" stroke-width="1.6"/></svg></li>
    <li>Create your own payment methods<svg width="14" height="11" viewBox="0 0 14 11"><path d="M1 6l4 4 8-9" fill="none" stroke="#8fc35a" stroke-width="1.6"/></svg></li>
    <li>Product variations<svg width="14" height="11" viewBox="0 0 14 11"><path d="M1 6l4 4 8-9" fill="none" stroke="#8fc35a" stroke-width="1.6"/></svg></li>
    <li>Built-in analysis tools<svg width="14" height="11" viewBox="0 0 14 11"><path d="M1 6l4 4 8-9" fill="none" stroke="#8fc35a" stroke-width="1.6"/></svg></li>
  </ul>
</div>
<div class="photo-celebrate" role="img" aria-label="Photo of a cheerful woman sitting on the floor with a laptop, arms raised in celebration"></div>
<a class="btn-outline" style="left:483px;top:1759px;width:231px;height:49px">CREATE YOUR WEBSHOP &raquo;</a>

<h2 class="section-title" style="top:1881px">Get straight to growing your business</h2>
<p class="band-lead" style="top:1930px">Itaque earum rerum hic tenetur a sapiente delectus, ut aut reiciendis voluptatibus<br>maiores alias consequatur aut perferendis doloribus asperiores repellat</p>
<div class="photo-store" role="img" aria-label="Photo of a smiling woman holding a product box in a busy store aisle"></div>
<a class="btn-outline" style="left:483px;top:2325px;width:231px;height:49px">GET STARTED NOW &raquo;</a>

<section class="device-band">
  <h2>Look Great on<br>Any Device</h2>
  <div class="rule"></div>
  <p>Duis aute irure dolor in reprehenderit in voluptate velit esse cillum dolore eu fugiat nulla pariatur. Excepteur sint occaecat cupidatat non proident, sunt in culpa qui officia deserunt mollit anim id est laborum.</p>
  <a class="btn-yellow">CREATE YOUR WEBSHOP &raquo;</a>
  <div class="device-preview" role="img" aria-label="Image of a smartphone displaying the mobile version of the Vendlyx landing page"></div>
</section>

<footer class="site-footer">
  <div class="copy">©Copyright information here</div>
  <div class="social"><span></span><span></span><span></span></div>
</footer>

</body>
</html>
```